Career Drop Down Layout on CopperTrailhead.com Quiz Results

We want to redesign the career drop down view after people take the career finder quiz at CopperTrailhead.com. After you take the quiz (feel free to take it yourself), you get a results page. On the left hand navigation bar, go to Career Matches (in green). When you open one of your career matches, we want people to see lots of great information about the job. We need help figuring out how to display the information. The information we want to display is the following:

1) name of job
2) JOBLEX description
3) Link to the Joblex info
4) Match dial
5) Bright outlook image
6) a video about the job
7) Average salary
8) Minimum Qualifications
9) Top Tips
10) Recommended Programs
11) Jobs in their area - by Hire Lantern

I put screen shots of what we have now and a mock-up of the new elements in the brief. It can look anyway you think will be good. I'm not tied to the mock-up at all.

To see how your design will look live on the web do the following:

1) Login at: https://www.coppertrailhead.com/survey/login (or take the quiz yourself to see your own results)
2) Enter Email address: dana.kowal@copperventure.org
3) Enter Password: 123456
4) See results summary - Click on Career Matches from the left navigation bar
5) See the career matches, when you click the arrow on the right side of each career match it will display the new page you are designing for each career with info from a database.

Thanks, Dana

Target Market(s)

Young people looking for jobs

Number of Pages Required

1 page

Requirements
Must have
• The layout of how all the information will look nicely on a computer screen. It can scroll down more vertically if necessary.

The color scheme and text must match the existing site since this page will be embedded in our site. I attached our design guide.
Nice to have
• I'd like to see a very easy to scan, organized way to display a lot of job information.

```html
<!DOCTYPE html>
<html lang="en">
<head>
<meta charset="utf-8">
<title>Life Coaching – Career Match</title>
<link rel="stylesheet" href="https://fonts.googleapis.com/css2?family=Nunito:wght@400;500;600;700&display=swap">
<style>
:root{
  --bg-a:#e6f1de;
  --bg-b:#e4e3f2;
  --panel-green:#f0f4ec;
  --panel-mint:#f5faf1;
  --panel-lilac:#eeeefa;
  --card-lilac:#e4e4f7;
  --indigo:#3b2f74;
  --indigo-text:#3c3580;
  --ink:#2b2b2b;
  --muted:#555;
  --line:#d5d9d4;
  --salary-top:#b7dca0;
}
*{box-sizing:border-box;margin:0;padding:0}
html,body{width:1200px;height:1133px;overflow:hidden}
body{
  font-family:"Nunito",sans-serif;
  background:linear-gradient(135deg,var(--bg-a),var(--bg-b));
  position:relative;color:var(--ink);
}
.shell{position:absolute;left:132px;top:89px;width:935px;height:954px;border-radius:22px;
  background:rgba(240,243,238,.55);border:1px solid rgba(255,255,255,.8);
  box-shadow:0 20px 50px rgba(120,130,150,.12)}
.panel{position:absolute;border-radius:26px}
.summary{left:155px;top:111px;width:187px;height:909px;background:var(--panel-green);text-align:center}
.gauge{position:absolute;left:21px;top:22px}
.match-label{position:absolute;top:110px;width:100%;font-size:12.5px;color:var(--ink)}
.salary{position:absolute;left:22px;top:202px;width:146px;height:85px;border-radius:8px;
  background:linear-gradient(180deg,var(--salary-top),var(--panel-green))}
.salary h3{font-weight:600;font-size:13px;margin-top:32px;color:var(--ink)}
.salary p{font-weight:700;font-size:17px;margin-top:10px}
.outlook{position:absolute;left:95px;top:349px;width:78px;height:67px;margin-left:-39px;border-radius:8px;background:#dde9f2}
.outlook span{position:absolute;left:21px;top:16px;width:36px;height:36px;border-radius:5px;background:#2a7fd4}
.quals{position:absolute;top:470px;width:100%;font-size:12.5px}
.quals .label{color:var(--muted)}
.quals .value{margin-top:9px}
.summary-rule{position:absolute;left:13px;top:617px;width:161px;border:0;border-top:1px solid var(--line)}
.jobs-by{position:absolute;top:718px;width:100%;font-size:12px;display:flex;justify-content:center;align-items:center;gap:12px}
.jobs-by i{display:inline-block;width:34px;height:11px;background:#34393b}
.jobs-brand{position:absolute;top:770px;width:100%;display:flex;justify-content:center;align-items:center;gap:8px;font-size:21px;font-weight:600;color:#3a3f42}
.jobs-brand b{display:inline-block;width:16px;height:16px;background:#8fd12b}

.description{left:364px;top:111px;width:447px;height:415px;background:var(--panel-mint);padding:29px 55px 0 15px}
.description h2{font-size:13px;font-weight:600}
.description p{font-size:13.1px;line-height:22.4px;margin-top:12px;color:#2d2d2d}
.description p+p{margin-top:11px}
.btn{display:block;margin-top:39px;width:405px;height:33px;border-radius:9px;background:var(--indigo);color:#fff;text-align:center;line-height:33px;font-size:13.5px;text-decoration:none}
.insider{display:block;width:405px;text-align:center;margin-top:18px;font-size:13.3px;color:var(--ink)}

.media{left:364px;top:549px;width:447px;height:471px;background:var(--panel-mint)}
.video{position:absolute;left:23px;top:90px;width:401px;height:292px;border-radius:8px;
  background:radial-gradient(ellipse at center,#d2d2d2 0%,#bdbdbd 55%,#8c8c8c 100%);
  box-shadow:0 4px 12px rgba(0,0,0,.15)}
.play{position:absolute;left:172px;top:117px}

.career{left:833px;top:111px;width:212px;height:112px;background:var(--panel-lilac)}
.reactions{position:absolute;top:23px;left:17px;width:180px;display:flex;justify-content:space-between}
.career h1{position:absolute;left:19px;top:68px;font-size:17px;font-weight:600;color:var(--indigo-text)}

.tips{left:833px;top:248px;width:212px;height:772px;background:var(--panel-lilac)}
.tips h2{position:absolute;left:19px;top:38px;font-size:14.5px;font-weight:600;color:var(--indigo-text)}
.bulb{position:absolute;left:19px;top:83px}
.tip-text{position:absolute;left:19px;top:128px;width:154px;font-size:11.2px;line-height:22.5px;color:var(--indigo-text)}
.pager{position:absolute;left:63px;top:222px;display:flex;align-items:center;gap:14px}
.dot{width:8px;height:8px;border-radius:50%;background:#4d4690}
.dot.off{background:#a8a6cf}
.tips-rule{position:absolute;left:18px;top:277px;width:159px;border:0;border-top:1px solid #d3d3e4}
.programs{position:absolute;left:18px;top:312px;width:157px;height:361px;border-radius:10px;background:var(--card-lilac);padding:0 24px;color:var(--indigo-text)}
.programs h3{font-size:14px;font-weight:500;line-height:22.5px;margin-top:25px}
.badge{width:41px;height:41px;background:#5aa6c4;margin-top:26px}
.badge.wide{width:54px;height:26px;background:#2f5bb8;border-radius:3px;margin-top:27px}
.prog-name{font-size:13.5px;line-height:22.5px;margin-top:14px;color:#4a4690}
.prog-name.second{margin-top:41px}
.program-rule{border:0;border-top:1px solid #d3d3ea;margin:13px -4px 0 0}
.view-all{position:absolute;left:41px;top:687px;font-size:11.5px;line-height:22.5px;color:#5a5590;text-decoration:underline}
</style>
</head>
<body>
<div class="shell"></div>

<section class="panel summary">
  <svg class="gauge" width="144" height="81" viewBox="0 0 178 100" aria-label="Match dial">
    <path d="M17 95 A72 72 0 0 1 161 95" fill="none" stroke="#d3d3d3" stroke-width="22"/>
    <path d="M89 95 L29 95 A60 60 0 0 1 40.5 59.7Z" fill="#d9262a"/>
    <path d="M89 95 L40.5 59.7 A60 60 0 0 1 70.5 37.9Z" fill="#ef8a25"/>
    <path d="M89 95 L70.5 37.9 A60 60 0 0 1 107.5 37.9Z" fill="#f5d033"/>
    <path d="M89 95 L107.5 37.9 A60 60 0 0 1 137.5 59.7Z" fill="#7bbf3f"/>
    <path d="M89 95 L137.5 59.7 A60 60 0 0 1 149 95Z" fill="#4b3a9a"/>
    <path id="dial-arc" d="M23 95 A66 66 0 0 1 155 95" fill="none"/>
    <text font-family="Nunito,sans-serif" font-size="6" font-weight="700" fill="#333"><textPath href="#dial-arc" startOffset="8%" text-anchor="middle">LOW</textPath></text>
    <text font-family="Nunito,sans-serif" font-size="6" font-weight="700" fill="#333"><textPath href="#dial-arc" startOffset="30%" text-anchor="middle">FAIR</textPath></text>
    <text font-family="Nunito,sans-serif" font-size="6" font-weight="700" fill="#333"><textPath href="#dial-arc" startOffset="50%" text-anchor="middle">GOOD</textPath></text>
    <text font-family="Nunito,sans-serif" font-size="6" font-weight="700" fill="#333"><textPath href="#dial-arc" startOffset="68%" text-anchor="middle">GREAT</textPath></text>
    <text font-family="Nunito,sans-serif" font-size="6" font-weight="700" fill="#333"><textPath href="#dial-arc" startOffset="88%" text-anchor="middle">EXCELLENT</textPath></text>
    <circle cx="89" cy="95" r="18" fill="#fff"/>
    <polygon points="86,91 92,99 141,76" fill="#222"/>
    <circle cx="89" cy="95" r="7" fill="#222"/>
  </svg>
  <p class="match-label">Your match level (12)</p>
  <div class="salary"><h3>Average Salary</h3><p>$35,950</p></div>
  <div class="outlook" role="img" aria-label="Bright outlook badge"><span></span></div>
  <div class="quals"><p class="label">Minimum Qualifications</p><p class="value">None</p></div>
  <hr class="summary-rule">
  <p class="jobs-by"><i></i>Jobs by</p>
  <p class="jobs-brand"><b></b>Hire Lantern</p>
</section>

<section class="panel description">
  <h2>JOBLEX job description:</h2>
  <p>Counsel individuals to maximize the independence and employability of persons coping with personal, social, and vocational difficulties that result from birth defects, illness, disease, accidents, aging, or the stress of daily life.</p>
  <p>Coordinate activities for residents of care and treatment facilities. Assess client needs and design and implement rehabilitation programs that may include personal and vocational counseling, training, and job placement.</p>
  <a class="btn" href="#">Learn more about this job on JOBLEX</a>
  <a class="insider" href="#">Industry Insider Page</a>
</section>

<section class="panel media">
  <div class="video" role="img" aria-label="Copper Trailhead introduction video about life coaching">
    <svg class="play" width="58" height="58" viewBox="0 0 58 58" aria-hidden="true">
      <circle cx="29" cy="29" r="29" fill="rgba(110,120,100,.55)"/>
      <path d="M21 15 L44 29 L21 43Z" fill="none" stroke="#fff" stroke-width="2.5" stroke-linejoin="round"/>
    </svg>
  </div>
</section>

<section class="panel career">
  <div class="reactions">
    <svg width="38" height="38" viewBox="0 0 38 38" aria-label="Like">
      <circle cx="19" cy="19" r="18" fill="#b5d9a2" stroke="#9cc58a"/>
      <path d="M11 18h5v10h-5zM16 18l5-8c2 0 3 1 2 4l-1 3h5c2 0 2 2 1 3l-2 7c-1 1-2 1-3 1h-7z" fill="#9cc984" stroke="#7fb06a"/>
    </svg>
    <svg width="38" height="38" viewBox="0 0 38 38" aria-label="Maybe">
      <circle cx="19" cy="19" r="17" fill="#6a6a6a" stroke="#333" stroke-width="2"/>
      <path d="M15 25V12a2 2 0 0 1 4 0v7m0-3a2 2 0 0 1 4 0v3m0-2a2 2 0 0 1 4 0v7c0 4-3 6-6 6h-2c-3 0-5-3-7-6l-2-3a2 2 0 0 1 3-2l2 2" fill="#fff" stroke="#222" stroke-width="1.6" stroke-linejoin="round"/>
    </svg>
    <svg width="38" height="38" viewBox="0 0 38 38" aria-label="Dislike">
      <circle cx="19" cy="19" r="18" fill="#e8a0a6" stroke="#d4838a"/>
      <path d="M11 10h5v10h-5zM16 20l5 8c2 0 3-1 2-4l-1-3h5c2 0 2-2 1-3l-2-7c-1-1-2-1-3-1h-7z" fill="#e2939a" stroke="#c9717a"/>
    </svg>
  </div>
  <h1>Life Coaching</h1>
</section>

<section class="panel tips">
  <h2>Top Tips</h2>
  <svg class="bulb" width="28" height="28" viewBox="0 0 28 28" aria-hidden="true" fill="none" stroke="#4b4590" stroke-width="1.6">
    <path d="M8 21h8M9 24h6M12 3a7 7 0 0 0-4 12.5c1 .8 1 2 1 3h6c0-1 0-2.2 1-3A7 7 0 0 0 12 3z"/>
    <path d="M21 3v4M19 5h4M24 9h2"/>
  </svg>
  <p class="tip-text">You don't need any formal training to become a life coach, but we recommend it.</p>
  <div class="pager">
    <svg width="10" height="14" viewBox="0 0 10 14"><path d="M8 1L2 7l6 6" fill="none" stroke="#4b4590" stroke-width="1.6"/></svg>
    <span class="dot"></span><span class="dot off"></span>
    <svg width="10" height="14" viewBox="0 0 10 14"><path d="M2 1l6 6-6 6" fill="none" stroke="#4b4590" stroke-width="1.6"/></svg>
  </div>
  <hr class="tips-rule">
  <div class="programs">
    <h3>Preferred Online Programs</h3>
    <div class="badge"></div>
    <p class="prog-name">Coach Craft Institute</p>
    <hr class="program-rule">
    <div class="badge wide"></div>
    <p class="prog-name second">Global Coaching Guild</p>
  </div>
  <a class="view-all" href="#">View Life Coaching<br>Programs</a>
</section>
</body>
</html>
```